Heater product information sheets

I need the two product information sheets organized and laid out in a clean, easy to read attractive manner. These sheets are to advertise propane heaters for outdoor use and for wholesale to propane distributors, restaurants and homeowners that need to have propane heat as the winter ends and spring begins. They will be used for chilly evenings when people want to be outside eating, drinking and being social.
Updates

Low design quality

Target Market(s)

Restaurants, hospitality industry, special events, party rental companies, home owners with backyards

Font styles to use
Sans Serif

Requirements
Must have
• My logo in the document instead of k. Dahlby and company
Nice to have
• I would like to see Fire illustrated coming up the heaters and on the round glass, show it up the middle of the glass tube propane heater.

```html
<!DOCTYPE html>
<html lang="en">
<head>
<meta charset="utf-8">
<title>Outdoor Propane Heater – Product Sheet</title>
<link rel="stylesheet" href="https://fonts.googleapis.com/css2?family=Poppins:wght@200;300;400;500;600&family=Josefin+Sans:wght@300;600&display=swap">
<style>
:root{
  --ink:#1b1a1b;
  --orange:#ef8246;
  --paper:#f7f7f7;
  --band:#ececed;
  --tag:#e6e6e7;
  --text:#3a3a3a;
  --white:#ffffff;
  --backdrop:#e9e9e9;
}
*{margin:0;padding:0;box-sizing:border-box}
html,body{width:1180px;height:1200px;overflow:hidden;background:var(--backdrop)}
.canvas{position:relative;width:1180px;height:1200px}
.sheet{
  position:absolute;left:140px;top:14px;width:790px;height:1029px;
  transform:scale(1.14);transform-origin:0 0;
  background:var(--paper);font-family:'Poppins',sans-serif;color:var(--text);overflow:hidden;
  box-shadow:0 10px 30px rgba(0,0,0,.12);
}
.header{position:absolute;left:0;top:0;width:790px;height:259px;background:var(--ink)}
.flame-visual{position:absolute;left:515px;top:0;width:275px;height:259px;
  background:radial-gradient(ellipse at 55% 60%,#f08a3c 0%,#d0501c 38%,#5a1e0a 70%,#1b1a1b 100%)}
.heater-visual{position:absolute;left:578px;top:259px;width:114px;height:378px;
  background:linear-gradient(90deg,#1d1d1f 0%,#3d3d40 45%,#1a1a1c 100%);
  border-radius:20px 20px 30px 30px}
.title{position:absolute;left:50px;top:64px;line-height:1}
.title-main{display:block;font-family:'Josefin Sans',sans-serif;font-weight:300;font-size:82px;color:var(--white);letter-spacing:0}
.title-sub{display:block;margin-top:6px;font-family:'Josefin Sans',sans-serif;font-weight:600;font-size:48px;color:var(--orange);letter-spacing:0}
.tag{position:absolute;left:54px;height:32px;padding:0 12px 0 14px;background:var(--tag);border-left:4px solid var(--orange);
  font-size:18px;font-weight:500;letter-spacing:2px;color:#333;line-height:33px}
.tag-specs{top:244px}
.tag-details{top:375px}
.list{position:absolute;list-style:none;font-size:12.5px;color:#333}
.list li{position:relative;padding-left:22px;line-height:16px;margin-bottom:5px}
.list svg{position:absolute;left:0;top:1px;width:14px;height:14px}
.specs-a{left:54px;top:293px}
.specs-a li{margin-bottom:9px}
.specs-b{left:322px;top:295px;width:230px}
.specs-b li{margin-bottom:8px}
.details{left:54px;top:420px}
.details li{margin-bottom:4.9px}
.hatch{position:absolute;left:0;top:654px;width:790px;height:10px;
  background:repeating-linear-gradient(135deg,#bdbdbd 0 1.5px,transparent 1.5px 5px)}
.uses{position:absolute;left:0;top:664px;width:790px;height:68px;background:var(--band)}
.use{position:absolute;top:0;height:68px;display:flex;align-items:center;gap:14px;
  font-size:12px;font-weight:600;line-height:15.5px;color:var(--ink);text-transform:uppercase}
.use svg{width:38px;height:38px}
.use-events{left:52px}.use-restaurants{left:330px}.use-home{left:575px}
.contact-panel{position:absolute;left:0;top:732px;width:477px;height:275px;background:var(--ink);color:var(--white);text-align:center}
.cta{position:absolute;left:0;width:458px;top:10px;font-weight:200;font-size:45px;line-height:50px;letter-spacing:.5px}
.rule{position:absolute;left:67px;width:322px;height:2px;background:#cfcfcf}
.rule-top{top:113px}.rule-bottom{top:217px}
.brand{position:absolute;left:0;width:458px;top:126px;display:flex;justify-content:center;align-items:center;gap:8px;
  font-weight:600;font-size:38px;letter-spacing:1px;color:var(--white)}
.brand-dot{width:14px;height:14px;background:var(--orange);border-radius:50%}
.brand-name{position:absolute;left:0;width:458px;top:186px;font-size:13px;font-weight:500}
.contact{position:absolute;left:0;width:458px;top:224px;font-size:14px;line-height:20px}
.offer-panel{position:absolute;left:477px;top:732px;width:313px;height:275px;background:var(--orange)}
.offers{list-style:none;position:absolute;left:36px;top:28px;color:var(--ink);font-size:17px;font-weight:500;line-height:21px;text-transform:uppercase}
.offers li{position:relative;padding-left:40px}
.offers li+li{margin-top:26px}
.offers svg{position:absolute;left:0;top:2px;width:26px;height:26px}
</style>
</head>
<body>
<div class="canvas">
  <article class="sheet">
    <header class="header">
      <div class="flame-visual" role="img" aria-label="Photo of orange flames behind the top of a patio heater"></div>
      <h1 class="title"><span class="title-main">OUTDOOR</span><span class="title-sub">PROPANE HEATER</span></h1>
    </header>
    <div class="heater-visual" role="img" aria-label="Photo of a black patio propane heater pole and base"></div>

    <h2 class="tag tag-specs">SPECIFICATIONS</h2>
    <ul class="list specs-a">
      <li><svg viewBox="0 0 14 14"><circle cx="7" cy="7.5" r="5.5" fill="none" stroke="#ef8246" stroke-width="1.6"/><path d="M4.3 7.3l2.2 2.2 6-6.5" fill="none" stroke="#ef8246" stroke-width="1.8"/></svg>Powerful 48,000 BTU</li>
      <li><svg viewBox="0 0 14 14"><circle cx="7" cy="7.5" r="5.5" fill="none" stroke="#ef8246" stroke-width="1.6"/><path d="M4.3 7.3l2.2 2.2 6-6.5" fill="none" stroke="#ef8246" stroke-width="1.8"/></svg>Black Powder Coated Finish</li>
    </ul>
    <ul class="list specs-b">
      <li><svg viewBox="0 0 14 14"><circle cx="7" cy="7.5" r="5.5" fill="none" stroke="#ef8246" stroke-width="1.6"/><path d="M4.3 7.3l2.2 2.2 6-6.5" fill="none" stroke="#ef8246" stroke-width="1.8"/></svg>Uses 20 lbs. Propane Tank</li>
      <li><svg viewBox="0 0 14 14"><circle cx="7" cy="7.5" r="5.5" fill="none" stroke="#ef8246" stroke-width="1.6"/><path d="M4.3 7.3l2.2 2.2 6-6.5" fill="none" stroke="#ef8246" stroke-width="1.8"/></svg>CE, GS, AGA, CSA, with ETL<br>certificate and ROHS approved</li>
    </ul>

    <h2 class="tag tag-details">ADDITIONAL DETAILS</h2>
    <ul class="list details">
      <li><svg viewBox="0 0 14 14"><circle cx="7" cy="7.5" r="5.5" fill="none" stroke="#ef8246" stroke-width="1.6"/><path d="M4.3 7.3l2.2 2.2 6-6.5" fill="none" stroke="#ef8246" stroke-width="1.8"/></svg>Commercial Quality</li>
      <li><svg viewBox="0 0 14 14"><circle cx="7" cy="7.5" r="5.5" fill="none" stroke="#ef8246" stroke-width="1.6"/><path d="M4.3 7.3l2.2 2.2 6-6.5" fill="none" stroke="#ef8246" stroke-width="1.8"/></svg>For Outdoor Use Only</li>
      <li><svg viewBox="0 0 14 14"><circle cx="7" cy="7.5" r="5.5" fill="none" stroke="#ef8246" stroke-width="1.6"/><path d="M4.3 7.3l2.2 2.2 6-6.5" fill="none" stroke="#ef8246" stroke-width="1.8"/></svg>Conforms to ANSI STD Z83.26-2014 Certified to CSA</li>
      <li><svg viewBox="0 0 14 14"><circle cx="7" cy="7.5" r="5.5" fill="none" stroke="#ef8246" stroke-width="1.6"/><path d="M4.3 7.3l2.2 2.2 6-6.5" fill="none" stroke="#ef8246" stroke-width="1.8"/></svg>STD 2.37-2014 Gas- fired outdoor infrared patio heaters<br>Safety Auto Shut Off Switch</li>
      <li><svg viewBox="0 0 14 14"><circle cx="7" cy="7.5" r="5.5" fill="none" stroke="#ef8246" stroke-width="1.6"/><path d="M4.3 7.3l2.2 2.2 6-6.5" fill="none" stroke="#ef8246" stroke-width="1.8"/></svg>Thermostatic Control</li>
      <li><svg viewBox="0 0 14 14"><circle cx="7" cy="7.5" r="5.5" fill="none" stroke="#ef8246" stroke-width="1.6"/><path d="M4.3 7.3l2.2 2.2 6-6.5" fill="none" stroke="#ef8246" stroke-width="1.8"/></svg>Base Diameter 17" - Anti-Tip Design</li>
      <li><svg viewBox="0 0 14 14"><circle cx="7" cy="7.5" r="5.5" fill="none" stroke="#ef8246" stroke-width="1.6"/><path d="M4.3 7.3l2.2 2.2 6-6.5" fill="none" stroke="#ef8246" stroke-width="1.8"/></svg>Standard Wheels - Tilt &amp; Move</li>
      <li><svg viewBox="0 0 14 14"><circle cx="7" cy="7.5" r="5.5" fill="none" stroke="#ef8246" stroke-width="1.6"/><path d="M4.3 7.3l2.2 2.2 6-6.5" fill="none" stroke="#ef8246" stroke-width="1.8"/></svg>Run time: 8-10 hours with standard 20 lbs. Propane tank</li>
      <li><svg viewBox="0 0 14 14"><circle cx="7" cy="7.5" r="5.5" fill="none" stroke="#ef8246" stroke-width="1.6"/><path d="M4.3 7.3l2.2 2.2 6-6.5" fill="none" stroke="#ef8246" stroke-width="1.8"/></svg>88" Tall</li>
      <li><svg viewBox="0 0 14 14"><circle cx="7" cy="7.5" r="5.5" fill="none" stroke="#ef8246" stroke-width="1.6"/><path d="M4.3 7.3l2.2 2.2 6-6.5" fill="none" stroke="#ef8246" stroke-width="1.8"/></svg>Heating Area: 200 sq. ft</li>
    </ul>

    <div class="hatch"></div>
    <section class="uses">
      <div class="use use-events"><svg viewBox="0 0 24 24"><path d="M12 2.5l2.9 6.1 6.6.8-4.9 4.6 1.3 6.6L12 17.3l-5.9 3.3 1.3-6.6-4.9-4.6 6.6-.8z" fill="#ef8246" stroke="#ef8246" stroke-width="1.5" stroke-linejoin="round"/></svg><span>Rentals for<br>live events</span></div>
      <div class="use use-restaurants"><svg viewBox="0 0 24 24"><path d="M12 2.5l2.9 6.1 6.6.8-4.9 4.6 1.3 6.6L12 17.3l-5.9 3.3 1.3-6.6-4.9-4.6 6.6-.8z" fill="#ef8246" stroke="#ef8246" stroke-width="1.5" stroke-linejoin="round"/></svg><span>Rentals for<br>restaurants &amp;<br>catering halls</span></div>
      <div class="use use-home"><svg viewBox="0 0 24 24"><path d="M12 2.5l2.9 6.1 6.6.8-4.9 4.6 1.3 6.6L12 17.3l-5.9 3.3 1.3-6.6-4.9-4.6 6.6-.8z" fill="#ef8246" stroke="#ef8246" stroke-width="1.5" stroke-linejoin="round"/></svg><span>Purchase for<br>your home or<br>business</span></div>
    </section>

    <section class="contact-panel">
      <p class="cta">TO RENT<br>OR PURCHASE</p>
      <div class="rule rule-top"></div>
      <div class="brand"><span class="brand-dot"></span><span>NER</span></div>
      <p class="brand-name">Northfield Event Rental</p>
      <div class="rule rule-bottom"></div>
      <p class="contact">555-014-2290 &nbsp;|&nbsp; jordan@northfieldrental.com<br>42 Depot Street Millbrook, NJ 07000</p>
    </section>

    <section class="offer-panel">
      <ul class="offers">
        <li><svg viewBox="0 0 26 26"><path d="M21 12.5A8.5 8.5 0 1 1 16 5" fill="none" stroke="#1b1a1b" stroke-width="2.6" stroke-linecap="round"/><path d="M8.5 12l3.5 3.5 10-10.5" fill="none" stroke="#1b1a1b" stroke-width="2.8" stroke-linecap="round" stroke-linejoin="round"/></svg>Starting at<br>$250 each</li>
        <li><svg viewBox="0 0 26 26"><path d="M21 12.5A8.5 8.5 0 1 1 16 5" fill="none" stroke="#1b1a1b" stroke-width="2.6" stroke-linecap="round"/><path d="M8.5 12l3.5 3.5 10-10.5" fill="none" stroke="#1b1a1b" stroke-width="2.8" stroke-linecap="round" stroke-linejoin="round"/></svg>Discounts for<br>large quantity<br>orders</li>
        <li><svg viewBox="0 0 26 26"><path d="M21 12.5A8.5 8.5 0 1 1 16 5" fill="none" stroke="#1b1a1b" stroke-width="2.6" stroke-linecap="round"/><path d="M8.5 12l3.5 3.5 10-10.5" fill="none" stroke="#1b1a1b" stroke-width="2.8" stroke-linecap="round" stroke-linejoin="round"/></svg>Assembly &amp;<br>delivery available<br>upon request</li>
      </ul>
    </section>
  </article>
</div>
</body>
</html>
```